velmorix - customer deliverable template

Word Template Design for Client Deliverables

We are looking for a professional and polished Word template for our client deliverables, including RFP responses, business proposals, technical proposals, and workshop reports. The template must be fully aligned with our corporate style and branding.

To kick things off, we'll start with our ML Pathfinder Session deliverable document as the base for the new template. This is a very simple project with very limited effort.

Project Resources
All necessary documentation and assets can be found in the following Brenvault Files folder:
https://files.brenvault.example/share/7kQ2wPzrT9xLmA4vBn8cYdE5fHjU3sR?ref=link

The folder includes:
Assets: A folder containing our logos, corporate color palettes, and other design inspiration to help you understand our style.
For additional inspiration, please visit our website: www.velmorix.cloud

Feel free to ask any questions you may have.

Best regards,

Velmorix Team

```html
<!DOCTYPE html>
<html lang="en">
<head>
<meta charset="utf-8">
<title>Velmorix – ML Pathfinder Session Template</title>
<link rel="stylesheet" href="https://fonts.googleapis.com/css2?family=Poppins:wght@500;600;700&family=Open+Sans:wght@600;700&family=Carlito:ital,wght@0,400;0,700;1,400&display=swap">
<style>
  :root{
    --stage:#d6dedd;
    --navy:#0a1a3f;
    --navy-deep:#0a0f1e;
    --ink:#14213d;
    --text:#1b1b1b;
    --green:#38d88f;
    --paper:#ffffff;
    --paper-soft:#f4f7f6;
    --panel:#f3f5f4;
  }
  *{margin:0;padding:0;box-sizing:border-box}
  html,body{width:1200px;height:1200px;overflow:hidden;background:var(--stage)}
  body{position:relative;font-family:"Carlito",Calibri,sans-serif;color:var(--text)}
  .page{position:absolute;width:394px;height:558px;background:var(--paper);overflow:hidden}
  .page--cover{left:188px;top:29px;background:var(--navy-deep)}
  .page--summary{left:617px;top:29px;background:var(--paper-soft)}
  .page--overview{left:188px;top:614px}
  .page--prep{left:617px;top:614px}

  /* cover */
  .cover-art{position:absolute;left:0;top:0;width:394px;height:437px;
    background:
      radial-gradient(ellipse 230px 180px at 100% 0%, #35d690 0%, rgba(40,160,130,.55) 35%, rgba(12,40,80,0) 75%),
      linear-gradient(180deg,#0b1c45 0%,#0a2350 45%,#0b1838 100%);}
  .brand-mark{position:absolute;left:45px;top:58px;display:flex;align-items:center;gap:6px;
    font-family:"Poppins",sans-serif;font-weight:600;font-size:27px;color:#fff;line-height:1}
  .brand-mark .sq{width:13px;height:13px;background:var(--green)}
  .cover-title{position:absolute;left:48px;top:176px;font-family:"Open Sans",sans-serif;font-weight:600;
    font-size:27px;line-height:40px;color:#fff}
  .cover-rule{position:absolute;left:48px;top:262px;width:62px;height:2.5px;background:var(--green)}
  .cover-band{position:absolute;left:0;top:437px;width:394px;height:67px;background:#fff}
  .client-name{position:absolute;left:61px;top:25px;font-family:"Poppins",sans-serif;font-weight:500;font-size:9px;line-height:10px;color:#2a2a2a;text-align:center}
  .client-name small{display:block;font-size:7px;font-weight:500}
  .customer{position:absolute;left:167px;top:26px;font-family:"Open Sans",sans-serif;font-weight:600;font-size:9.5px;color:#111}

  /* text */
  p{font-size:6px;line-height:8.1px}
  .justify p{text-align:justify}
  .h-summary{position:absolute;left:56px;top:139px;font-family:"Poppins",sans-serif;font-weight:700;font-size:16.5px;color:var(--green);letter-spacing:.1px}
  .col{position:absolute;top:171px;width:130px}
  .col p+p{margin-top:8px}
  .col--a{left:56px}.col--b{left:208px}
  .purpose{position:absolute;left:45px;top:369px;width:302px;height:83px;background:var(--green);padding:8px 12px}
  .purpose h3{font-family:"Poppins",sans-serif;font-weight:600;font-size:8px;color:#fff;margin-bottom:8px}
  .purpose p{color:#fff;text-align:justify;font-size:5.6px;line-height:8px}

  .h-section{position:absolute;left:53px;font-family:"Poppins",sans-serif;font-weight:600;font-size:10.5px;line-height:16px;color:var(--ink)}
  .h-section span{display:inline-block;width:12px}
  .flow{position:absolute;left:56px;width:281px}
  .lead{margin-bottom:9px}
  .sub{font-weight:700;font-size:5.8px;color:var(--green);margin-bottom:6px}
  .phase{padding:4px;margin-bottom:2px}
  .phase--shaded{background:var(--panel)}
  .phase h4{font-weight:700;font-size:6.3px;color:var(--ink);margin-bottom:4px}
  .phases-diagram{position:absolute;left:80px;top:372px;width:234px;height:64px}
  .caption{position:absolute;left:0;width:394px;top:447px;text-align:center;font-style:italic;font-size:5.2px}

  .h-sub{font-weight:700;font-size:6.8px;color:var(--green);margin:9px 0}
  .flow--prep p+p{margin-top:7px}

  .footer{position:absolute;left:56px;top:521px;width:282px;border-top:.8px solid var(--green);padding-top:7px;display:flex;align-items:center}
  .footer-mark{font-family:"Poppins",sans-serif;font-weight:600;font-size:7px;color:var(--ink);display:flex;align-items:center;gap:2px;width:55px}
  .footer-mark .sq{width:4px;height:4px;background:var(--green)}
  .footer-title{font-size:4.6px;color:var(--ink);flex:1}
  .footer-num{font-size:4.6px}
</style>
</head>
<body>

<section class="page page--cover">
  <div class="cover-art" role="img" aria-label="Dark navy backdrop with a green glow and faint city silhouettes"></div>
  <div class="brand-mark"><span class="sq"></span>velmorix</div>
  <h1 class="cover-title">ML Pathfinder<br>Session</h1>
  <div class="cover-rule"></div>
  <div class="cover-band">
    <div class="client-name">BRAND NAME<small>Your Tagline Here</small></div>
    <div class="customer">Customer Name</div>
  </div>
</section>

<section class="page page--summary">
  <h2 class="h-summary">EXECUTIVE SUMMARY</h2>
  <div class="col col--a justify">
    <p>In today's dynamic business landscape, Artificial Intelligence stands as a pivotal force for innovation and competitive differentiation. However, many organizations find themselves navigating a complex AI labyrinth, struggling to identify tangible applications and realize a genuine return on investment. The challenge isn't just about understanding AI's theoretical capabilities, but about pinpointing its most impactful and viable applications within your unique operational context.</p>
    <p>At velmorix, we understand that unlocking AI's true potential requires a strategic, well-defined starting point. Our ML Pathfinder Session is meticulously designed to serve as that foundational step. It's a collaborative exploration, guided by our expert team, aimed at demystifying AI and translating its vast possibilities into concrete business value for your organization.</p>
  </div>
  <div class="col col--b justify">
    <p>This report summarizes the key insights and actionable recommendations derived from our joint workshop. It provides you with a clear, prioritized roadmap of the most impactful AI use cases tailored to your business, assessed based on both their potential impact and practical feasibility. Consider this your essential starting point, laying a solid foundation for a successful and strategic AI implementation journey.</p>
  </div>
  <div class="purpose">
    <h3>PURPOSE OF THIS DOCUMENT</h3>
    <p>The Purpose of this Document is to provide a comprehensive overview and detailed outcome of the ML Pathfinder Session conducted by velmorix with Customer Name. This report serves as a critical deliverable, synthesizing our collaborative efforts to identify, analyze, and prioritize the most impactful and feasible Artificial Intelligence use cases for your business. It is designed to equip your organization with a clear, actionable roadmap, empowering you to make informed decisions and confidently embark on your strategic AI implementation journey.</p>
  </div>
</section>

<section class="page page--overview">
  <h2 class="h-section" style="top:47px"><span>1.</span>Workshop Overview: The Three Phases of AI<br><span></span>Discovery</h2>
  <div class="flow" style="top:89px">
    <p class="lead">Our ML Pathfinder Session is designed to cut through the complexity of artificial intelligence and pinpoint its most impactful applications for your business. We believe a successful AI journey starts with a clear vision and a structured approach. That's why our workshop is built around three distinct, yet interconnected, phases: Inspire, Discover, and Prioritize. This methodical framework ensures we don't just identify AI possibilities but truly understand their relevance to your operations and map out a viable path to implementation.</p>
    <div class="sub">Our Approach: The Three Phases of AI Discovery</div>
    <div class="phase phase--shaded">
      <h4>Inspire: Igniting Possibilities</h4>
      <p>In this dynamic 60-minute initial phase, our goal is to inspire you by broadening your perspective on AI's potential. We take you on a journey through various AI approaches, from foundational Artificial Intelligence to groundbreaking AI Agents. With a focus on real-world examples and success stories tailored to your industry, we help you envision a future where AI creates tangible value. This isn't just about understanding the technology; it's about seeing how AI can transform your vision into reality.</p>
    </div>
    <div class="phase">
      <h4>Discover: Unearthing Core Opportunities</h4>
      <p>In this 60-minute collaborative session, our team of experts guides you to uncover core AI use cases unique to your business. We organize you into small groups of three to brainstorm and discuss a wide range of possibilities, from optimizing operations to enhancing customer experiences. With our guidance, each group identifies and select the three most impactful use cases that align with your strategic goals. This hands-on phase transforms potential into a concrete, actionable plan.</p>
    </div>
    <div class="phase phase--shaded">
      <h4>Prioritize: Defining Your Strategic Roadmap</h4>
      <p>During this final 90-minute session, each team presents their top three use cases to the entire group. We then facilitate a collective evaluation, using a robust methodology to rank each idea based on its potential business impact and feasibility of implementation. This process is designed to prioritize the most promising opportunities and ensure your efforts are focused where they deliver the greatest return. The result is not just a list of ideas, but a final list of quick wins you can start implementing right away, giving a clear, actionable roadmap for your AI journey.</p>
    </div>
  </div>
  <svg class="phases-diagram" viewBox="0 0 234 64" aria-label="Inspire, Discover and Prioritize phases joined by arrows">
    <g font-family="Poppins, sans-serif" text-anchor="middle" fill="#fff">
      <circle cx="36" cy="32" r="30" fill="#3ddc97" stroke="#14213d" stroke-width="1.3"/>
      <text x="36" y="32" font-size="8.5" font-weight="600">Inspire</text>
      <text x="36" y="39" font-size="4.2" font-weight="600">(60 minutes)</text>
      <circle cx="116" cy="32" r="30" fill="#6a0dbe" stroke="#14213d" stroke-width="1.3"/>
      <text x="116" y="32" font-size="8.5" font-weight="600">Discover</text>
      <text x="116" y="39" font-size="4.2" font-weight="600">(60 minutes)</text>
      <circle cx="196" cy="32" r="30" fill="#a0a00a" stroke="#14213d" stroke-width="1.3"/>
      <text x="196" y="32" font-size="8.5" font-weight="600">Prioritize</text>
      <text x="196" y="39" font-size="4.2" font-weight="600">(90 minutes)</text>
    </g>
    <g stroke="#14213d" stroke-width="0.9" fill="none">
      <path d="M68 32h14M78 28.5l4 3.5-4 3.5"/>
      <path d="M148 32h14M158 28.5l4 3.5-4 3.5"/>
    </g>
  </svg>
  <div class="caption">Figure 1. The Three Phases of AI Discovery</div>
  <div class="footer">
    <div class="footer-mark"><span class="sq"></span>velmorix</div>
    <div class="footer-title">ML Pathfinder Session for Customer Name</div>
    <div class="footer-num">4</div>
  </div>
</section>

<section class="page page--prep">
  <h2 class="h-section" style="top:53px"><span>2.</span>Discovery Workshop Preparation</h2>
  <div class="flow flow--prep" style="top:83px">
    <p>To ensure a productive and truly impactful session, we've designed a meticulous preparation phase tailored to Customer Name organization's unique needs. This groundwork is essential for a collaborative environment where every participant can contribute meaningfully, and the outcomes are directly applicable to your business.</p>
    <h3 class="h-sub">A Foundation of Diverse Expertise</h3>
    <p>We believe that the best solutions emerge from a variety of perspectives. To that end, we have collaborated with you to identify a diverse group of employees who participated in the workshop. This group included individuals from various roles, functions, and levels of IT expertise. This strategic selection ensures we capture a comprehensive view of your business, from high-level strategic goals to on-the-ground operational realities. A list of these participants is included in Annex 1 for your reference.</p>
    <h3 class="h-sub">Leveraging Participant Insights</h3>
    <p>Prior to the workshop, each selected participant has been asked to complete a preparatory survey. This detailed questionnaire, which can be found in Annex 2, allows us to gather invaluable insights. We inquired about their specific roles, their expectations for the session, their understanding of the company's strategic goals, and any other relevant information they wish to share. This proactive data collection is a cornerstone of our methodology.</p>
    <h3 class="h-sub">Customizing Your Workshop Experience</h3>
    <p>The insights we gain from these surveys allow us to fully customize your workshop. The content, real-world examples, and discussion topics will be precisely adapted to your industry and business context, ensuring the session is immediately relevant and engaging. Furthermore, we will adjust the level of technical vocabulary and the pace of the discussion to match the audience's knowledge level. This is crucial for making the workshop understandable for everyone, preventing participants from getting lost in technical jargon, and ensuring that all voices are heard and valued.</p>
    <p style="margin-top:9px">Our goal is to create an environment where every participant feels empowered to contribute, resulting in a more collaborative and effective outcome for your organization.</p>
  </div>
  <div class="footer">
    <div class="footer-mark"><span class="sq"></span>velmorix</div>
    <div class="footer-title">ML Pathfinder Session for Customer Name</div>
    <div class="footer-num">5</div>
  </div>
</section>

</body>
</html>
```